IT Company dealing Business to Business website

Built on Wordpress
Professional eye-catching website, mobile friendly and responsive
We are currently in the process of re branding the company and refreshing the current image. The current website contains the necessary information about the company and services we provide. Also detailing companies we partner with.
We have a new logo and tag line which we are eager to incorporate into the new website.
We wish to have a fresh elegant business website which reflects our company value and delivers vital information for both old and new clients about what we provide in terms of service.
The website should be an extension of our offline media and an integrated company overview.

Target Market(s)

Businesses who require IT services

Industry/Entity Type

It Company

Coding

Coded - Design and coding required

Number of Pages Required

5+ page

Font styles to use
Sans Serif

Colors

Designer to choose colors to be used in the design.

Requirements
Must have
• Be made in Wordpress, and editable after without needing coding
• Mobile friendly/responsive
• Remote links to be displayed at the top of the web page
• Pay account and customer portal also displayed at the top of the web page
• Partners of the company to be displayed at the bottom of the screen
Nice to have
• Scrolling image in the centre, to be used for advertising services/features

```html
<!DOCTYPE html>
<html lang="en">
<head>
<meta charset="utf-8">
<title>Corelink Solutions – IT Support</title>
<link href="https://fonts.googleapis.com/css2?family=Poppins:wght@300;400;500;600&display=swap" rel="stylesheet">
<style>
:root{
  --blue:#0a6cc4;
  --blue-dark:#08589f;
  --red:#ef4b5a;
  --ink:#333a44;
  --muted:#7b838c;
  --line:#d8dde3;
  --soft:#f1f2f4;
  --dark:#1f2328;
  --footer:#232528;
  --white:#fff;
}
*{margin:0;padding:0;box-sizing:border-box}
html,body{width:1200px;height:2736px;overflow:hidden}
body{font-family:'Poppins',sans-serif;color:var(--ink);background:var(--white);position:relative}
.abs{position:absolute}
a{color:inherit;text-decoration:none}

/* top bar */
.topbar{left:0;top:0;width:1200px;height:40px;background:var(--blue);color:var(--white);font-size:10px}
.topbar .tag{left:98px;top:13px}
.topbar .remote{left:650px;top:13px}
.topbar .rdot{top:10px;width:20px;height:20px;border-radius:50%;border:1.5px solid rgba(255,255,255,.8)}
.topbar .rdot.on{background:var(--white)}
.topbar .helpdesk{left:972px;top:7px;width:128px;height:26px;border-radius:13px;background:var(--white);color:var(--blue);font-size:11px;font-weight:500;text-align:center;line-height:26px}

/* header */
.logo{left:100px;top:80px;display:flex;align-items:center;gap:10px}
.logo .mark{width:30px;height:30px;background:var(--blue)}
.logo .name{font-size:27px;font-weight:600;color:var(--blue);letter-spacing:.5px}
.nav{left:370px;top:89px;display:flex;gap:34px;font-size:12px;font-weight:500;color:var(--ink)}
.nav .active{color:var(--blue)}
.call{left:784px;top:80px;color:var(--blue);font-size:16px;font-weight:500}
.call small{display:block;font-size:10px;color:var(--muted);font-weight:400;margin-top:-2px;padding-left:14px}
.paynow{left:972px;top:78px;width:128px;height:38px;border-radius:19px;background:var(--red);color:var(--white);font-size:12px;font-weight:500;text-align:center;line-height:38px}

/* hero */
.hero-title{left:98px;top:190px;width:260px;font-size:31px;line-height:37px;font-weight:400;color:var(--blue)}
.hero-sub{left:98px;top:344px;font-size:19px;color:var(--muted)}
.hero-note{left:98px;top:374px;font-size:11px;color:var(--muted)}
.btn-outline{border:1.5px solid var(--blue);border-radius:20px;color:var(--blue);font-size:11px;font-weight:500;text-align:center}
.hero-btn{left:98px;top:537px;width:114px;height:38px;line-height:35px}
.photo{overflow:hidden}
.hero-main{left:359px;top:157px;width:482px;height:480px;background:linear-gradient(135deg,#6e6a66,#2b2a2c 60%,#4a4744)}
.hero-main .cap{left:40px;bottom:70px;color:var(--white);width:400px}
.cap h3{font-size:19px;font-weight:500;margin-bottom:6px}
.cap p{font-size:11px;line-height:16px}
.cap .more{font-size:11px;margin-top:20px;display:block}
.hero-side{left:881px;width:219px;height:219px}
.hero-side .cap{left:24px;bottom:60px;color:var(--white);font-size:14px;font-weight:500;line-height:18px}
.side-a{top:157px;background:linear-gradient(135deg,#e8e2da,#b9a99a 55%,#7f6e60)}
.side-b{top:418px;background:linear-gradient(135deg,#6d7c8c,#3a4654 55%,#262d36)}
.arrow-btn{width:36px;height:36px;border-radius:50%;border:1.5px solid var(--blue);display:flex;align-items:center;justify-content:center}

/* about band */
.about{left:0;top:677px;width:1200px;height:560px;background:var(--blue)}
.about .big{left:99px;top:41px;width:480px;height:480px;border-radius:50%;background:radial-gradient(circle at 40% 40%,#dfe2e6,#9ea4ab 55%,#4b5057)}
.about .small{left:401px;top:340px;width:176px;height:176px;border-radius:50%;border:6px solid var(--white);background:linear-gradient(#2b3f66,#13203a 60%,#c79a4c)}
.about h2{left:620px;top:120px;width:480px;font-size:21px;line-height:26px;font-weight:500;color:var(--white)}
.about p{left:620px;width:478px;font-size:11.5px;line-height:16px;color:#e6eef8}
.about .btn{left:620px;top:396px;width:111px;height:36px;line-height:34px;border:1.5px solid var(--white);color:var(--white);border-radius:18px;font-size:11px;font-weight:500;text-align:center}

/* solutions */
.section-title{width:1200px;left:0;text-align:center;font-size:20px;font-weight:500;color:var(--blue)}
.sol{width:308px;top:1364px;height:330px}
.sol .img{height:161px}
.sol h4{font-size:14px;font-weight:500;color:var(--blue);margin:26px 0 8px}
.sol p{font-size:11.5px;line-height:17px;color:var(--muted)}
.sol .more{position:absolute;left:0;top:302px;font-size:11px;color:var(--muted)}
.img-a{background:linear-gradient(180deg,#fbfbfb 0,#f1efe9 62%,#ea6a1f 80%,#d94f0e)}
.img-b{background:linear-gradient(180deg,#dfe6ee,#9aa9ba 55%,#4a5a6a)}
.img-c{background:linear-gradient(90deg,#e9eaeb,#3b6fb5 40%,#3f9b48 60%,#2a5ea8 85%,#e9eaeb)}

/* support band */
.support{left:0;top:1742px;width:1200px;height:396px;background:linear-gradient(135deg,#2a3038,#15191e 60%,#252a31);color:var(--white)}
.support h2{left:0;width:1200px;top:58px;text-align:center;font-size:20px;font-weight:500}
.support .lead{left:370px;width:460px;top:90px;text-align:center;font-size:11.5px;line-height:16px;color:#d8dce0}
.feat{top:170px;width:230px}
.feat svg{display:block;margin-bottom:8px}
.feat h5{font-size:14px;font-weight:500;margin-bottom:6px}
.feat p{font-size:11px;line-height:16px;color:#c9ced4}
.support .btn{left:543px;top:296px;width:114px;height:38px;line-height:35px;border:1.5px solid var(--white);border-radius:19px;font-size:11px;text-align:center}

/* partners */
.partner{top:2251px;width:184px;height:96px;background:var(--soft)}
.partner .badge{position:absolute;left:52px;top:36px;width:80px;height:24px;border-radius:4px;background:#cfd4da}
.parrow{top:2281px}
.parrow.fill{background:var(--blue);border-color:var(--blue)}

/* footer */
.footer{left:0;top:2411px;width:1200px;height:325px;background:var(--footer);color:#a9adb2;font-size:11px}
.footer .logo{left:98px;top:56px}
.footer .copy{left:98px;top:118px;line-height:17px}
.footer .links{left:98px;top:172px;color:#c5c9cd}
.footer .links .on{color:var(--blue)}
.footer h6{font-size:13px;font-weight:500;color:var(--blue)}
.footer .phone{font-size:21px;color:#c5c9cd;font-weight:300}
.footer .pill{border:1.5px solid #676b70;border-radius:16px;text-align:center;color:#c5c9cd}
.social{top:100px;width:30px;height:30px;border-radius:50%;border:1.5px solid #676b70}
</style>
</head>
<body>

<!-- top bar -->
<div class="abs topbar">
  <span class="abs tag">IT support service solutions throughout Western Australia.</span>
  <span class="abs remote">Remvio remote Support:</span>
  <span class="abs rdot" style="left:816px"></span>
  <span class="abs rdot on" style="left:851px"></span>
  <span class="abs rdot" style="left:886px"></span>
  <a class="abs helpdesk">Helpdesk Login</a>
</div>

<!-- header -->
<div class="abs logo"><span class="mark"></span><span class="name">CORELINK</span></div>
<nav class="abs nav">
  <a class="active">IT Services ⌄</a><a>Solutions ⌄</a><a>News/Blog</a><a>Contact Us</a>
</nav>
<div class="abs call">Call: (08) 5550 1234<small>E. info@corelink.example</small></div>
<a class="abs paynow">$&nbsp; Pay Now</a>

<!-- hero -->
<h1 class="abs hero-title">We provide a<br>hassle free<br>IT service and<br>support</h1>
<div class="abs hero-sub">Our clients love us.</div>
<div class="abs hero-note">Try us and you will too.</div>
<a class="abs btn-outline hero-btn">IT Services</a>

<div class="abs photo hero-main" role="img" aria-label="Office headset resting on a laptop keyboard">
  <div class="abs cap">
    <h3>Professional IT services</h3>
    <p>Pellentesque ac justo fringilla, efficitur eros eget, ullamcorper velit. Mauris id interdum metus.</p>
    <span class="more">Learn More &nbsp;→</span>
  </div>
</div>
<div class="abs photo hero-side side-a" role="img" aria-label="Business team in a meeting">
  <div class="abs cap">IT Management<br>Service</div>
</div>
<div class="abs photo hero-side side-b" role="img" aria-label="Consultant at work in an office">
  <div class="abs cap">Consultations<br>Service</div>
</div>
<div class="abs arrow-btn" style="left:1120px;top:516px"><svg width="12" height="12" viewBox="0 0 12 12"><path d="M7.5 2 3.5 6l4 4" fill="none" stroke="#0a6cc4" stroke-width="1.6"/></svg></div>
<div class="abs arrow-btn" style="left:1120px;top:560px"><svg width="12" height="12" viewBox="0 0 12 12"><path d="M4.5 2l4 4-4 4" fill="none" stroke="#0a6cc4" stroke-width="1.6"/></svg></div>

<!-- about -->
<section class="abs about">
  <div class="abs big" role="img" aria-label="Laptop wrapped in chains and a padlock"></div>
  <div class="abs small" role="img" aria-label="City skyline at night over water"></div>
  <h2 class="abs">Corelink Solutions is a Perth IT support service providing businesses with complete IT support service solutions throughout Western Australia.</h2>
  <p class="abs" style="top:242px">We provide IT support for small businesses through to medium sized enterprises to ensure they gain maximum benefit from their computing and IT environment. Keeping your equipment up to date and running smoothly is our focus so you can focus on your business.</p>
  <p class="abs" style="top:320px">With our Perth Help Desk IT program, and Perth IT Service Support programs, Corelink Solutions removes the problem for business owners maintaining their IT and computer services.</p>
  <a class="abs btn">About Us</a>
</section>

<!-- solutions -->
<h2 class="abs section-title" style="top:1312px">Solution We Provide</h2>
<div class="abs sol" style="left:98px">
  <div class="img img-a" role="img" aria-label="Cloud office suite product banner"></div>
  <h4>Offivo Suite</h4>
  <p>Get the value and simplicity of Offivo Suite for small businesses, a set of web-enabled tools that let you access your email, documents contacts, and ...</p>
  <span class="more">Learn More &nbsp;→</span>
</div>
<div class="abs sol" style="left:445px">
  <div class="img img-b" role="img" aria-label="Desk phone in a modern office"></div>
  <h4>VOIP</h4>
  <p>Talvoro Standard offers unrivalled features for SMBs (up to 100 users) at a competitive price with unmatched stability and simplicity. It supports various combinations ...</p>
  <span class="more" style="color:#0a6cc4">Learn More &nbsp;→</span>
</div>
<div class="abs sol" style="left:792px">
  <div class="img img-c" role="img" aria-label="Software product boxes"></div>
  <h4>Plandrix Pro</h4>
  <p>With Plandrix, you can achieve a paperless work flow with powerful PDF creation, markup, editing and collaboration features. Create high quality PDFs with one-click from ...</p>
  <span class="more">Learn More &nbsp;→</span>
</div>

<!-- support -->
<section class="abs support" role="img" aria-label="Technician working in a server room" style="overflow:hidden">
  <h2 class="abs">Fast, Reliable IT Support</h2>
  <p class="abs lead">When you experience IT problems, we're there for you. Corelink Solutions offers help desk solutions, including:</p>
  <div class="abs feat" style="left:98px">
    <svg width="30" height="30" viewBox="0 0 24 24"><path d="M6.6 10.8a15 15 0 0 0 6.6 6.6l2.2-2.2c.3-.3.7-.4 1-.2 1.1.4 2.3.6 3.6.6.6 0 1 .4 1 1V20c0 .6-.4 1-1 1A17 17 0 0 1 3 4c0-.6.4-1 1-1h3.5c.6 0 1 .4 1 1 0 1.3.2 2.5.6 3.6.1.3 0 .7-.2 1z" fill="#2b8ae0"/></svg>
    <h5>Phone Support</h5><p>Ut enim ad minim veniam, quis nostrud exercitation ullamco laboris.</p>
  </div>
  <div class="abs feat" style="left:359px">
    <svg width="34" height="30" viewBox="0 0 28 24"><rect x="2" y="3" width="18" height="13" rx="1" fill="none" stroke="#2b8ae0" stroke-width="2"/><rect x="19" y="8" width="7" height="13" rx="1" fill="#2b8ae0"/><path d="M6 20h10" stroke="#2b8ae0" stroke-width="2"/></svg>
    <h5>Remote Support</h5><p>Ut enim ad minim veniam, quis nostrud exercitation ullamco laboris.</p>
  </div>
  <div class="abs feat" style="left:620px">
    <svg width="30" height="30" viewBox="0 0 24 24"><circle cx="12" cy="12" r="10" fill="#2b8ae0"/><circle cx="9" cy="10" r="1.3" fill="#1a1e23"/><circle cx="15" cy="10" r="1.3" fill="#1a1e23"/><path d="M8 14.5c2 2 6 2 8 0" stroke="#1a1e23" stroke-width="1.6" fill="none"/></svg>
    <h5>On Site Support</h5><p>Ut enim ad minim veniam, quis nostrud exercitation ullamco laboris.</p>
  </div>
  <div class="abs feat" style="left:879px">
    <svg width="30" height="30" viewBox="0 0 24 24"><rect x="4" y="3" width="16" height="19" rx="2" fill="#2b8ae0"/><circle cx="12" cy="10" r="3" fill="#1a1e23"/><path d="M7 18c1-3 9-3 10 0" fill="#1a1e23"/></svg>
    <h5>Contact Us</h5><p style="font-size:14px;color:#fff">Call: (08) 5550 1234</p><p>E. info@corelink.example</p>
  </div>
  <a class="abs btn">Contact Us</a>
</section>

<!-- partners -->
<h2 class="abs section-title" style="top:2198px">Our Partners</h2>
<div class="abs arrow-btn parrow" style="left:42px"><svg width="12" height="12" viewBox="0 0 12 12"><path d="M7.5 2 3.5 6l4 4" fill="none" stroke="#0a6cc4" stroke-width="1.6"/></svg></div>
<div class="abs partner" style="left:98px"><span class="badge"></span></div>
<div class="abs partner" style="left:302px"><span class="badge"></span></div>
<div class="abs partner" style="left:507px"><span class="badge"></span></div>
<div class="abs partner" style="left:711px"><span class="badge"></span></div>
<div class="abs partner" style="left:916px"><span class="badge"></span></div>
<div class="abs arrow-btn parrow fill" style="left:1120px"><svg width="12" height="12" viewBox="0 0 12 12"><path d="M4.5 2l4 4-4 4" fill="none" stroke="#fff" stroke-width="1.6"/></svg></div>

<!-- footer -->
<footer class="abs footer">
  <div class="abs logo"><span class="mark"></span><span class="name">CORELINK</span></div>
  <div class="abs copy">© Copyright 2018 Corelink Solutions<br>All Rights Reserved.</div>
  <div class="abs links"><span class="on">Home</span> &nbsp;|&nbsp; About &nbsp;|&nbsp; Blog</div>

  <h6 class="abs" style="left:447px;top:68px">Need Help? Contact us</h6>
  <div class="abs phone" style="left:447px;top:96px">Call: (08) 5550 1234</div>
  <div class="abs" style="left:447px;top:126px">E. info@corelink.example</div>
  <div class="abs" style="left:447px;top:160px;line-height:17px">Location<br>PO Box 210 Riverside,<br>WA 6000</div>
  <a class="abs pill" style="left:447px;top:236px;width:112px;height:30px;line-height:27px">Contact Us</a>

  <h6 class="abs" style="left:793px;top:68px">Connect with Us</h6>
  <span class="abs social" style="left:793px"></span>
  <span class="abs social" style="left:833px"></span>
  <span class="abs social" style="left:873px"></span>
  <span class="abs social" style="left:913px"></span>
  <a class="abs pill" style="left:793px;top:158px;width:128px;height:28px;line-height:25px">Helpdesk Login</a>

  <svg class="abs" style="left:1126px;top:66px" width="22" height="30" viewBox="0 0 22 30"><path d="M11 28V3M2 12l9-9 9 9" fill="none" stroke="#0a6cc4" stroke-width="2.4"/></svg>
</footer>

</body>
</html>
```